PSD website for property company

Please read the brief thoroughly.

We are looking for a new website for a property group that does property acquisitions, property development and property management.
They buy, build and lease core inner city industrial assets in Sydney, Australia.
They also invest in residential developments.

Site menu
- Home page
- Property – sub menus include – Leasing ; Projects ; Investments ; Property Management
- Capital and finance
- About
- Contact

They like this website
https://www.verlo.com.au/

They want the site to be clean, modern and bold.
They like few colors, even black and white is OK to submit

They have a logo and style guide and useable images here:
http://www.kumet.net/temp/PelorisWeb2019.zip
The zip file is also attached to this project.
We have supplied some images to give you an idea, but we will also require you to provide at least 3 extra images from stock photos.
Use your imagination.

I am expecting a lot of similar designs, so be aware the photos you choose will be really important.
They want really 3 good stock photos used and supplied without charge.
Please not too generic, I repeat the quality of the photos is important.
You may provide several photos (but not in multiple submissions please) and we will choose the best three to be provided.

The winner will be selected on a single home page design and required to provide;
All photos use in original format without charge
A second ‘standard page’ template design based on the winning home page design

```html
<!DOCTYPE html>
<html lang="en">
<head>
<meta charset="utf-8">
<title>Peloris – Your Property Solution</title>
<link href="https://fonts.googleapis.com/css2?family=Arimo:wght@400;700&display=swap" rel="stylesheet">
<style>
:root{
  --green:#56702f;
  --ink:#1d1d1d;
  --body:#6b6b6b;
  --white:#ffffff;
  --line:#2b2b2b;
  --bar:#262626;
}
*{box-sizing:border-box;margin:0;padding:0}
html,body{width:1200px;height:4736px;overflow:hidden}
body{position:relative;background:var(--white);font-family:"Arimo",Arial,sans-serif;color:var(--ink)}
.abs{position:absolute}
.photo{position:absolute}
.btn{position:absolute;display:flex;align-items:center;justify-content:center;gap:10px;font-size:14px;text-transform:uppercase;border:2px solid var(--line);color:var(--ink);letter-spacing:.2px}
.btn.light{border-color:var(--white);color:var(--white)}
.btn svg{width:22px;height:10px}

/* hero */
.hero{position:absolute;left:0;top:0;width:1200px;height:790px;background:linear-gradient(160deg,#6b6f72 0%,#8a8d8e 30%,#4d5c6c 65%,#2d4a6b 100%)}
.logo{position:absolute;font-weight:700;color:var(--white);letter-spacing:7px}
.hero .logo{left:81px;top:30px;font-size:30px}
.nav{position:absolute;top:38px;right:84px;display:flex;gap:28px;font-size:14px;color:var(--white)}
.hero-title{position:absolute;left:0;width:1200px;top:340px;text-align:center;color:var(--white);font-size:43px;font-weight:700}
.hero .btn{left:474px;top:415px;width:252px;height:48px}
.slides{position:absolute;left:1148px;top:312px;width:30px;text-align:center;color:var(--white);font-size:7px;line-height:1}
.slides span{display:block;height:39px}
.slides .on{font-size:18px;height:39px;margin-top:-6px}
.scroll{position:absolute;left:0;width:1200px;top:736px;text-align:center;color:var(--white);font-size:6px}
.scroll-line{position:absolute;left:599px;top:746px;width:1px;height:81px;background:#9a9a9a}

/* intro */
.intro-title{position:absolute;left:0;width:1200px;top:842px;text-align:center;font-size:31px;font-weight:700;line-height:39px}
.intro-sub{position:absolute;left:0;width:1200px;top:950px;text-align:center;font-size:14px;color:var(--body)}
.card{position:absolute;top:1014px;width:331px}
.card .photo{position:relative;width:331px;height:206px}
.card h3{font-size:28px;font-weight:700;margin-top:34px}
.card p{font-size:14px;line-height:24px;color:var(--body);margin-top:24px;padding-left:2px}
.card .btn{position:relative;margin-top:30px;margin-left:2px;width:151px;height:40px}

/* feature panels */
.panel{position:absolute;background:var(--green);color:var(--white)}
.panel h2{position:absolute;font-size:31px;font-weight:700}
.panel p{position:absolute;font-size:14px;line-height:24px}
.panel .btn{width:151px;height:41px}

.section-title{position:absolute;left:0;width:1200px;text-align:center;font-size:31px;font-weight:700}

/* newsletter */
.news{position:absolute;left:0;top:3770px;width:1200px;height:612px;background:linear-gradient(180deg,#4a4c4b 0%,#5c5d58 55%,#4f5a46 100%)}
.news h2{position:absolute;left:0;width:1200px;top:84px;text-align:center;color:var(--white);font-size:31px;font-weight:700}
.field{position:absolute;left:331px;width:546px;border:2px solid #d8d8d8;color:var(--white);font-size:14px;padding:10px 24px}
.news .btn{left:526px;top:479px;width:149px;height:41px}

/* footer */
.footer{position:absolute;left:0;top:4382px;width:1200px;height:301px;background:var(--green);color:var(--white)}
.footer .logo{left:79px;top:54px;font-size:36px;letter-spacing:9px}
.footer-about{position:absolute;left:79px;top:114px;width:330px;font-size:14px;line-height:24px}
.footer-more{position:absolute;left:79px;top:231px;display:flex;align-items:center;gap:12px;font-size:14px}
.footer-more i{display:flex;width:26px;height:26px;border:1px solid var(--white);border-radius:50%;align-items:center;justify-content:center;font-style:normal;font-size:12px}
.fcol{position:absolute;top:62px;font-size:14px;line-height:24px}
.fcol h4{font-size:19px;font-weight:700;margin-bottom:24px}
.bottom{position:absolute;left:0;top:4683px;width:1200px;height:53px;background:var(--bar);color:var(--white);font-size:13px}
.bottom .copy{position:absolute;left:79px;top:20px}
.social{position:absolute;right:86px;top:20px;display:flex;gap:28px}
.social span{width:12px;height:12px;border-radius:50%;background:var(--white)}
.social span:first-child{background:#6f6f6f}
</style>
</head>
<body>

<header class="hero" role="img" aria-label="Modern apartment building with glass balconies, viewed from below">
  <div class="logo">PELORIS</div>
  <nav class="nav"><span>Home</span><span>Property</span><span>Capital and finance</span><span>About</span><span>Contact</span></nav>
  <h1 class="hero-title">YOUR PROPERTY SOLUTION</h1>
  <div class="btn light">Explore our projects
    <svg viewBox="0 0 22 10"><path d="M0 5h20M15 1l5 4-5 4" fill="none" stroke="currentColor" stroke-width="1.4"/></svg></div>
  <div class="slides"><span>01</span><span class="on">02</span><span>03</span><span>04</span><span>05</span></div>
  <div class="scroll">Scroll Down</div>
</header>
<div class="scroll-line"></div>

<h2 class="intro-title">PELORIS – Family owned and operated,<br>community orientated</h2>
<p class="intro-sub">Putting 45 years of local experience to work for the Inner West</p>

<article class="card" style="left:79px">
  <div class="photo" role="img" aria-label="Hand placing a small wooden house between rent and buy signs" style="background:linear-gradient(135deg,#f2efea,#e0d8cf)"></div>
  <h3>Leasing</h3>
  <p>Lorem Ipsum is simply dummy text of the printing and typesetting industry. Lorem Ipsum has been the industry's standard dummy text ever since the 1500s.</p>
  <div class="btn">Read more <svg viewBox="0 0 22 10"><path d="M0 5h20M15 1l5 4-5 4" fill="none" stroke="currentColor" stroke-width="1.4"/></svg></div>
</article>
<article class="card" style="left:434px">
  <div class="photo" role="img" aria-label="Stacks of coins in front of a rising financial chart" style="background:linear-gradient(135deg,#9fbad3,#5d7f9f)"></div>
  <h3>Investment</h3>
  <p>Lorem Ipsum is simply dummy text of the printing and typesetting industry. Lorem Ipsum has been the industry's standard dummy text ever since the 1500s.</p>
  <div class="btn">Read more <svg viewBox="0 0 22 10"><path d="M0 5h20M15 1l5 4-5 4" fill="none" stroke="currentColor" stroke-width="1.4"/></svg></div>
</article>
<article class="card" style="left:789px">
  <div class="photo" role="img" aria-label="Hand holding a glowing house icon above a city at night" style="background:linear-gradient(135deg,#3c4650,#1c232b)"></div>
  <h3>Property Managment</h3>
  <p>Lorem Ipsum is simply dummy text of the printing and typesetting industry. Lorem Ipsum has been the industry's standard dummy text ever since the 1500s.</p>
  <div class="btn">Read more <svg viewBox="0 0 22 10"><path d="M0 5h20M15 1l5 4-5 4" fill="none" stroke="currentColor" stroke-width="1.4"/></svg></div>
</article>

<section class="panel" style="left:524px;top:1658px;width:595px;height:415px">
  <h2 style="left:203px;top:48px">Capital and finance</h2>
  <p style="left:205px;top:108px;width:340px">Lorem Ipsum is simply dummy text of the printing and typesetting industry. Lorem Ipsum has been the industry's standard dummy text ever since the 1500s, when an unknown printer took a galley of type and scrambled it to make a type specimen book. It has survived not only five centuries, but also the leap into electronic typesetting, remaining essentially unchanged.</p>
  <div class="btn light" style="left:206px;top:327px">Read more <svg viewBox="0 0 22 10"><path d="M0 5h20M15 1l5 4-5 4" fill="none" stroke="currentColor" stroke-width="1.4"/></svg></div>
</section>
<div class="photo" role="img" aria-label="Dark brick curved apartment building on a street corner under a cloudy sky" style="left:83px;top:1603px;width:595px;height:397px;background:linear-gradient(180deg,#c9d6e0 0%,#a9b3b8 40%,#5a4a40 70%,#6f6a60 100%)"></div>

<h2 class="section-title" style="top:2158px">Recently Projects</h2>
<div class="photo" role="img" aria-label="Modern industrial building at sunset beside a road" style="left:85px;top:2255px;width:323px;height:210px;background:linear-gradient(180deg,#6f86a8,#b8b5b0 60%,#6b6b6e)"></div>
<div class="photo" role="img" aria-label="Red brick apartment tower against a blue sky" style="left:85px;top:2496px;width:323px;height:482px;background:linear-gradient(135deg,#8fb3d0,#b04a32 45%,#8a3526)"></div>
<div class="photo" role="img" aria-label="White high-rise with curved balconies against blue sky" style="left:439px;top:2253px;width:324px;height:480px;background:linear-gradient(135deg,#3d6fae,#dfe4ea 55%,#7e8c9b)"></div>
<div class="photo" role="img" aria-label="Glass office building with trees in front" style="left:439px;top:2764px;width:324px;height:212px;background:linear-gradient(180deg,#4f84c4,#9cb3c8 50%,#4d5f45)"></div>
<div class="photo" role="img" aria-label="Contemporary white and dark houses" style="left:794px;top:2253px;width:323px;height:212px;background:linear-gradient(180deg,#f0f0f0,#6e6e6e 60%,#3c3c3c)"></div>
<div class="photo" role="img" aria-label="White and timber clad apartment block in winter" style="left:794px;top:2496px;width:323px;height:482px;background:linear-gradient(135deg,#b9c8d6,#8a5a3e 50%,#dfe3e8)"></div>
<div class="btn" style="left:489px;top:3029px;width:222px;height:44px;gap:4px">View more projects <svg viewBox="0 0 22 10"><path d="M0 5h20M15 1l5 4-5 4" fill="none" stroke="currentColor" stroke-width="1.4"/></svg></div>

<section class="panel" style="left:79px;top:3198px;width:596px;height:417px">
  <h2 style="left:59px;top:48px">About us</h2>
  <p style="left:59px;top:109px;width:340px">Lorem Ipsum is simply dummy text of the printing and typesetting industry. Lorem Ipsum has been the industry's standard dummy text ever since the 1500s, when an unknown printer took a galley of type and scrambled it to make a type specimen book. It has survived not only five centuries, but also the leap into electronic typesetting, remaining essentially unchanged.</p>
  <div class="btn light" style="left:59px;top:329px">Read more <svg viewBox="0 0 22 10"><path d="M0 5h20M15 1l5 4-5 4" fill="none" stroke="currentColor" stroke-width="1.4"/></svg></div>
</section>
<div class="photo" role="img" aria-label="Arched dark brick building at dusk with an outdoor gathering in front" style="left:522px;top:3145px;width:595px;height:397px;background:linear-gradient(180deg,#b7bcc2 0%,#6d6a66 45%,#3a3630 100%)"></div>

<section class="news" role="img" aria-label="Arched brick building with garden, darkened as a background">
  <h2>Keep up to date</h2>
  <div class="field" style="top:162px;height:42px">Full Name</div>
  <div class="field" style="top:218px;height:43px">Phone#</div>
  <div class="field" style="top:275px;height:43px">Email Address</div>
  <div class="field" style="top:332px;height:131px">Message</div>
  <div class="btn light">Submit now <svg viewBox="0 0 22 10"><path d="M0 5h20M15 1l5 4-5 4" fill="none" stroke="currentColor" stroke-width="1.4"/></svg></div>
</section>

<footer class="footer">
  <div class="logo">PELORIS</div>
  <p class="footer-about">Lorem Ipsum is simply dummy text of the printing and typesetting industry. Lorem Ipsum has been the industry's standard dummy text ever since the 1500s.</p>
  <div class="footer-more">READ MORE <i>›</i></div>
  <div class="fcol" style="left:524px"><h4>Quick Links</h4>Home<br>Property<br>Capital and finance<br>About<br>Contact</div>
  <div class="fcol" style="left:750px"><h4>Useful Links</h4>Terms of Use<br>Privacy Policy<br>Customer Care</div>
  <div class="fcol" style="left:973px"><h4>Contact info...</h4>+00 123 456 789<br><br>info@peloris.com<br><br>72 Linden Court<br>Fairhaven, CA 93410</div>
</footer>
<div class="bottom">
  <span class="copy">Copyright © 2019 Peloris.All Right Resreved</span>
  <div class="social"><span></span><span></span><span></span><span></span><span></span><span></span></div>
</div>

</body>
</html>
```